modern, IT themed business card for IT accelerator

Design a business card for tech oriented business accelerator. Prevailing color shall be orange.
we are operating in emerging markets and our mission is to provide co-working space, mentorship/coaching and ultimately seed financing IT startups.
also, we are helping financed ITs in obtaining next round financing, and to this end we are meeting with non IT/finance people and investment professionals..
that means card shall be designed to "impress" not only IT people (mostly liberal) but finance (more conservative)

Industry/Entity Type

Investment

Contact Information for Business Card

Company Name: Orin Venture Yard
Name: Levan Kutateli
Position: Partner
Address: 14, Marjanishvili Ave., Tbilisi 0112, Georgia
Tel: +995599348817
Email: l.kutateli@orinyard.ge
Website: www.orinyard.ge

Font styles to use
Sans Serif

Requirements
Must have
• Attached are logos of the company (portrait & landscape) choose any
Nice to have
• industry is IT and finance (in fact, financing IT startups). therefore design might have IT theme (inspiration from web or software designs)

```html
<!DOCTYPE html>
<html lang="en">
<head>
<meta charset="utf-8">
<title>Orin Venture Yard – Business Card</title>
<link rel="stylesheet" href="https://fonts.googleapis.com/css2?family=Open+Sans:wght@400;600;700&display=swap">
<style>
  :root {
    --backdrop: #5a5a58;
    --card-white: #ffffff;
    --glow-center: #f6e22c;
    --glow-mid: #f6bf22;
    --glow-edge: #f2991c;
    --brand-olive: #7a6433;
    --site-ink: #4a4230;
    --name-ink: #1a1a1a;
    --accent-orange: #f29a1c;
    --label-ink: #555555;
    --value-ink: #8a8a8a;
    --ring-grey: #9a9a9a;
  }
  * { margin: 0; padding: 0; box-sizing: border-box; }
  html, body {
    width: 1200px;
    height: 509px;
    overflow: hidden;
    background: var(--backdrop);
    font-family: "Open Sans", Arial, sans-serif;
  }
  .stage { position: relative; width: 1200px; height: 509px; }

  .card {
    position: absolute;
    top: 100px;
    width: 507px;
    height: 293px;
    border-radius: 18px;
    overflow: hidden;
  }

  /* Front */
  .card-front {
    left: 98px;
    background: radial-gradient(ellipse 60% 75% at 50% 42%, var(--glow-center) 0%, var(--glow-mid) 45%, var(--glow-edge) 100%);
  }
  .front-mark {
    position: absolute;
    left: 50%;
    top: 50px;
    transform: translateX(-50%);
    display: flex;
    flex-direction: column;
    align-items: center;
  }
  .front-mark .mark-circle {
    width: 86px;
    height: 86px;
    border: 2px solid var(--brand-olive);
    border-radius: 50%;
    margin-bottom: 26px;
  }
  .front-mark .brand-name {
    font-weight: 600;
    font-size: 22px;
    color: var(--brand-olive);
    letter-spacing: 0.5px;
    white-space: nowrap;
  }
  .front-site {
    position: absolute;
    left: 0;
    right: 0;
    top: 226px;
    text-align: center;
    font-size: 14px;
    letter-spacing: 1px;
    color: var(--site-ink);
  }

  /* Back */
  .card-back {
    left: 620px;
    top: 101px;
    background: var(--card-white);
  }
  .holder-name {
    position: absolute;
    left: 48px;
    top: 64px;
    font-weight: 700;
    font-size: 14.5px;
    color: var(--name-ink);
    text-transform: uppercase;
  }
  .holder-role {
    position: absolute;
    left: 48px;
    top: 88px;
    font-size: 15px;
    color: var(--accent-orange);
  }
  .contact-list {
    position: absolute;
    left: 48px;
    top: 130px;
    width: 240px;
    list-style: none;
    font-size: 15px;
    line-height: 24px;
    color: var(--value-ink);
    white-space: nowrap;
    overflow: hidden;
  }
  .contact-list .label { color: var(--label-ink); }

  .back-mark {
    position: absolute;
    left: 306px;
    top: 30px;
    width: 182px;
    height: 182px;
    border: 3px solid var(--ring-grey);
    border-radius: 50%;
    display: flex;
    align-items: center;
    justify-content: center;
    text-align: center;
  }
  .back-mark .brand-name {
    font-weight: 600;
    font-size: 22px;
    line-height: 28px;
    color: var(--accent-orange);
  }
</style>
</head>
<body>
<main class="stage">
  <section class="card card-front" aria-label="Card front">
    <div class="front-mark">
      <span class="mark-circle" aria-hidden="true"></span>
      <span class="brand-name">Orin Venture Yard</span>
    </div>
    <p class="front-site">www.orinyard.ge</p>
  </section>

  <section class="card card-back" aria-label="Card back">
    <h1 class="holder-name">Levan Kutateli</h1>
    <p class="holder-role">Partner</p>
    <ul class="contact-list">
      <li><span class="label">Address:</span> 14, Marjanishvili Ave.</li>
      <li>Tbilisi 0112, Georgia</li>
      <li><span class="label">Tel:</span> +995599348817</li>
      <li><span class="label">Email:</span> l.kutateli@orinyard.ge</li>
    </ul>
    <div class="back-mark">
      <span class="brand-name">Orin<br>Venture<br>Yard</span>
    </div>
  </section>
</main>
</body>
</html>
```